Top Service Company Billboard for busiest highway in County

Top Service company seeks a NEW design for Billboard across highest traffic road in Country - more than 500,000 cars per day.

KRV is a residential services company, providing our clients with, Cleaning, maintenance, Pest Control and AC Duct Cleaning.

Please see ATTACHED specifications -

3 Must HAVES
Envision the company photo being the center/core of the message -
KRV Cleaning
Prices starting at AED 25

Target Market(s)

Residential Home Owners & Renters

Industry/Entity Type

Residential

Font styles to use
Serif

Colors

Designer to choose colors to be used in the design.

Requirements
Must have
• This Billboard must be in half Arabic and English - please see attached specifications
• As well please check attached for height & width requirements.
• This billboard must really pop -
• Envision the company photo being the center/core of the message -
• KRV Cleaning
• Prices starting at AED 25
• Need a catch phrase...
Nice to have
• + KRV Pest Control + Bravo Mend Up Logo if possible
Should not have
• Should not be English only

```html
<!DOCTYPE html>
<html lang="en">
<head>
<meta charset="utf-8">
<title>The Kind Help – Highway Billboard</title>
<link rel="stylesheet" href="https://fonts.googleapis.com/css2?family=Montserrat:wght@600;800;900&family=Cairo:wght@800&display=swap">
<style>
  :root {
    --sky-deep: #1468c8;
    --sky-mid: #3b95e6;
    --sky-light: #bfe3fb;
    --white: #ffffff;
    --orange: #f7931e;
    --navy: #1b2f6e;
    --ink: #111111;
    --photo-top: #9aa6b2;
    --photo-mid: #5a6470;
    --photo-low: #b48aa6;
  }
  html, body {
    margin: 0;
    padding: 0;
    width: 1200px;
    height: 92px;
    overflow: hidden;
  }
  .billboard {
    position: relative;
    width: 1200px;
    height: 92px;
    overflow: hidden;
    font-family: "Montserrat", Arial, sans-serif;
    background: linear-gradient(90deg, var(--sky-deep) 0%, var(--sky-mid) 22%, var(--sky-light) 34%, var(--sky-mid) 46%, var(--sky-mid) 66%, var(--sky-light) 80%, var(--sky-mid) 100%);
  }
  .headline {
    position: absolute;
    left: 24px;
    top: 11px;
    margin: 0;
    color: var(--white);
    font-weight: 800;
    font-size: 30px;
    letter-spacing: 0.5px;
    line-height: 1;
    white-space: nowrap;
    text-shadow: 0 1px 3px rgba(0,0,0,0.35);
  }
  .hotline {
    position: absolute;
    left: 56px;
    top: 50px;
    display: flex;
    align-items: center;
    gap: 7px;
    color: var(--white);
    font-weight: 800;
    font-size: 30px;
    line-height: 1;
    text-shadow: 0 1px 3px rgba(0,0,0,0.35);
  }
  .hotline svg { width: 32px; height: 32px; }
  .team-photo {
    position: absolute;
    left: 424px;
    top: 0;
    width: 376px;
    height: 92px;
    background: linear-gradient(180deg, var(--photo-top) 0%, var(--photo-mid) 45%, var(--photo-low) 75%, var(--photo-mid) 100%);
  }
  .price-badge {
    position: absolute;
    top: 8px;
    width: 76px;
    height: 76px;
    border-radius: 50%;
    background: var(--orange);
    border: 2px solid var(--white);
    box-sizing: border-box;
    color: var(--white);
    text-align: center;
    display: flex;
    flex-direction: column;
    justify-content: center;
    align-items: center;
    line-height: 1;
  }
  .price-badge.left { left: 366px; }
  .price-badge.right { left: 740px; }
  .badge-label { font-size: 7.5px; font-weight: 600; max-width: 52px; }
  .badge-amount { font-size: 30px; font-weight: 900; margin: 1px 0; }
  .badge-currency { font-size: 10px; font-weight: 800; }
  .arabic-name {
    position: absolute;
    right: 24px;
    top: 2px;
    margin: 0;
    color: var(--white);
    font-family: "Cairo", "Tahoma", sans-serif;
    font-weight: 800;
    font-size: 32px;
    line-height: 1.2;
    direction: rtl;
    text-shadow: 0 1px 3px rgba(0,0,0,0.3);
  }
  .service-brands {
    position: absolute;
    left: 872px;
    top: 56px;
    display: flex;
    gap: 14px;
    align-items: center;
  }
  .brand {
    display: flex;
    align-items: center;
    gap: 4px;
    color: var(--navy);
    font-weight: 800;
    font-size: 10px;
    white-space: nowrap;
  }
  .brand-mark {
    width: 12px;
    height: 12px;
    background: var(--navy);
    border-radius: 50%;
  }
</style>
</head>
<body>
  <main class="billboard">
    <h1 class="headline">THE KIND HELP</h1>
    <div class="hotline">
      <svg viewBox="0 0 32 32" aria-hidden="true">
        <circle cx="16" cy="16" r="14" fill="none" stroke="#ffffff" stroke-width="2.5"/>
        <path d="M11 8.5c1-.6 2-.3 2.5.6l1.3 2.6c.4.8.2 1.6-.5 2.1l-1 .8c.8 2 2.2 3.5 4.1 4.4l.8-1c.5-.7 1.4-.9 2.1-.5l2.6 1.3c.9.5 1.2 1.5.6 2.5-.9 1.5-2.5 2.3-4.2 1.8-4.7-1.4-8.2-5-9.6-9.6-.5-1.7.3-3.3 1.3-5z" fill="#ffffff"/>
      </svg>
      <span>800 KINDLY</span>
    </div>

    <div class="team-photo" role="img" aria-label="Company team photo: staff in uniform gathered in front of the service van fleet"></div>

    <div class="price-badge left">
      <span class="badge-label">Prices starting at</span>
      <span class="badge-amount">25</span>
      <span class="badge-currency">AED</span>
    </div>
    <div class="price-badge right">
      <span class="badge-label">Arabic translation</span>
      <span class="badge-amount">25</span>
      <span class="badge-currency">AED</span>
    </div>

    <h2 class="arabic-name" lang="ar">ذي كايند هلب</h2>

    <div class="service-brands">
      <span class="brand"><span class="brand-mark"></span>KRV Cleaning</span>
      <span class="brand"><span class="brand-mark"></span>KRV Pest Control</span>
      <span class="brand"><span class="brand-mark"></span>Bravo Mend Up</span>
    </div>
  </main>
</body>
</html>
```